Guided Study Tour - Klangtage Dornhalm Two Sided Flyer

We need a two-sided flyer for a Guided Study Tour to Klangtage Dornhalm. We want beautiful pictures of Germany and if possible some of the Velter venues our participants will be visiting. I have also provided the content that needs to be included. Also, in the attached document I provided a link to the Klangtage event. Please read and watch the video to be inspired.
This flyer should be beautiful and engaging. It needs to grab your attention right away and really highlight the wonderful things that they will be doing and that are included in the tour. This is a once in a lifetime opportunity for people to experience. We are targeting Music Directors and Music professionals.
Both attached logos need to be present on the flyer.

```html
<!DOCTYPE html>
<html lang="en">
<head>
<meta charset="utf-8">
<title>Guided Study Tour Flyer – Back</title>
<link rel="stylesheet" href="https://fonts.googleapis.com/css2?family=Poppins:wght@400;600;700&family=Lobster&family=Arimo:wght@400&display=swap">
<style>
:root{
  --stage:#f2f2f2;
  --red-light:#e0242a;
  --red-mid:#b8141c;
  --red-dark:#7a0a10;
  --blue:#1f4c9a;
  --blue-dark:#16336d;
  --gold:#f6a623;
  --bullet:#4ea6f2;
  --white:#ffffff;
  --band:#e2e2e2;
  --logo-blue:#2b3f8f;
  --logo-red:#c8202a;
}
*{margin:0;padding:0;box-sizing:border-box}
html,body{width:1200px;height:1200px;overflow:hidden;background:var(--stage)}
.flyer{
  position:absolute;left:257px;top:39px;width:790px;height:1121px;overflow:hidden;
  background:radial-gradient(ellipse at 50% 40%,var(--red-light) 0%,var(--red-mid) 45%,var(--red-dark) 100%);
  color:var(--white);
  font-family:"Poppins",sans-serif;
}
.wave{position:absolute;left:0;top:0;width:790px;height:1018px}
.content{position:absolute;left:24px;top:24px;width:744px}
.intro{font-size:19.6px;line-height:26.6px;letter-spacing:.1px}
.section-title{
  font-family:"Lobster",cursive;color:var(--gold);font-size:29px;line-height:34px;
  margin:14px 0 2px 4px;
}
.inclusions{list-style:none;font-size:19.6px;line-height:31.2px}
.inclusions li{position:relative;padding-left:26px}
.inclusions li::before{
  content:"";position:absolute;left:10px;top:12px;width:9px;height:9px;border-radius:50%;
  background:var(--bullet);
}
.contact{
  position:absolute;left:24px;top:738px;font-weight:700;color:var(--gold);
  font-size:19.6px;line-height:31px;letter-spacing:.2px;
}
.bio{
  position:absolute;left:24px;top:812px;width:742px;
  font-family:"Arimo",sans-serif;font-size:19.2px;line-height:24px;text-align:justify;
}
.bio-title{font-family:"Lobster",cursive;color:var(--gold);font-size:27px;margin-right:8px}
.partner-band{
  position:absolute;left:0;top:1018px;width:790px;height:103px;background:var(--band);
  display:flex;align-items:center;justify-content:space-around;
}
.partner{display:flex;align-items:center;gap:10px;font-family:"Poppins",sans-serif;font-weight:700;font-size:22px}
.partner-mark{width:18px;height:18px;border-radius:50%}
.partner--meridian{color:var(--logo-blue)}
.partner--meridian .partner-mark{background:var(--logo-blue)}
.partner--halden{color:var(--logo-red)}
.partner--halden .partner-mark{background:var(--logo-red);border-radius:0}
</style>
</head>
<body>
<main class="flyer">
  <svg class="wave" viewBox="0 0 790 1018" aria-hidden="true">
    <defs>
      <linearGradient id="waveFill" x1="0" y1="0" x2="0" y2="1">
        <stop offset="0" stop-color="#2c5db0"/>
        <stop offset="1" stop-color="#16336d"/>
      </linearGradient>
    </defs>
    <path d="M0 735 C120 760 240 790 360 768 C500 740 580 640 700 608 C740 598 770 596 790 594 L790 1018 L0 1018 Z" fill="url(#waveFill)"/>
  </svg>

  <div class="content">
    <p class="intro">Daniel Marsh partnered with Meridian Classic Tours &amp; Music Festivals to bring you and experience of a Lifetime. With over 100 years of combined educational student travel expertise, Meridian Classic Tours, powered by Halden Tours, brings unparalleled tour experiences for you and your students.</p>

    <h2 class="section-title">Trip Inclusions</h2>
    <ul class="inclusions">
      <li>Roundtrip Airfare from Houston</li>
      <li>13 Nights Accomodations, 3 Star Hotels with A/C</li>
      <li>Daily Breakfast</li>
      <li>Access to rehearsal sessions</li>
      <li>Pirvate Luxury Coach Transfer Services for airport transfers and day tours to Berlin, Weimar and Dresden &amp; Prague</li>
      <li>Professional Local Guides for for City Tours in: Berlin, Weimar, Dresden &amp; Prague</li>
      <li>Entrance Fees to: House of Anton Kessler, Franz Albrecht, Reinholt in Weimar, Lutheran Frauenkirche &amp; Alte Meister Gallery in the</li>
      <li>Zwiner Palace in Dresend, and Cathedral and Golden Lane in Prague</li>
      <li>All Applicable Taxes and Gratuities for Included Services, Guides, and Drivers</li>
      <li>$2 Million in Professional Liability Insurance</li>
      <li>24-hour Travel Support Staff</li>
    </ul>
  </div>

  <p class="contact">For more information contact Dr. Marsh at<br>d.marsh@ridgevale.edu</p>

  <p class="bio"><span class="bio-title">Daniel Marsh Bio:</span>Daniel Marsh is Director of Choral Studies at Ridgevale State University and the conductor of the Cedar Valley Chorale and the Cedar Choral Artists, a professional chamber choir. A native Texan, his degrees are from Harlow Pine University, Brenton University and the University of Westmoor. Recent engagements include conducting the Havelmann Requiem in Buffalo, NY, serving on the jury for the Aurelia International Choral Festival in Preveza, Greece and the International Choir Championship Vox Nova in Tusnia, Bosnia and Herzogevina.</p>

  <footer class="partner-band">
    <div class="partner partner--meridian"><span class="partner-mark"></span>Meridian Classic</div>
    <div class="partner partner--halden"><span class="partner-mark"></span>Halden Tours</div>
  </footer>
</main>
</body>
</html>
```